Anzeigengestaltung für Zahnarztpraxis
Zielgruppe
Zahnarztpraxis
Aufgabenstellung
Möchte eine moderne Stellenanzeige, ggf. einen zum Logo farblich passenden Rahmen; ggf. noch mit Bildern

```html
<!DOCTYPE html>
<html lang="de">
<head>
<meta charset="utf-8">
<title>Stellenanzeige Zahnarztpraxis Tannbach</title>
<link rel="stylesheet" href="https://fonts.googleapis.com/css2?family=Jost:wght@400;500;700&display=swap">
<style>
  :root {
    --navy: #13305c;
    --green: #7cb342;
    --ink: #1d1d1b;
    --paper: #ffffff;
    --fade-green: #a9cf8a;
    --photo-light: #ecebe6;
    --photo-mid: #d9d6d2;
    --glove: #8f94dc;
  }
  * { margin: 0; padding: 0; box-sizing: border-box; }
  html, body { width: 848px; height: 1200px; overflow: hidden; }
  body {
    font-family: "Jost", "Futura", sans-serif;
    color: var(--ink);
    background: var(--paper);
  }
  .poster {
    position: relative;
    width: 848px;
    height: 1200px;
    overflow: hidden;
    background: linear-gradient(to bottom, var(--paper) 0px, var(--paper) 800px, #e2eed5 960px, var(--fade-green) 1200px);
  }
  .hero-photo {
    position: absolute;
    left: 0; top: 0;
    width: 848px; height: 458px;
    background:
      radial-gradient(ellipse 200px 170px at 110px 270px, rgba(143,148,220,0.55), transparent 70%),
      radial-gradient(ellipse 120px 110px at 770px 250px, rgba(143,148,220,0.5), transparent 70%),
      radial-gradient(ellipse 220px 200px at 400px 200px, #f3f2ef, transparent 75%),
      linear-gradient(180deg, var(--photo-light), var(--photo-mid));
  }
  .brand-panel {
    position: absolute;
    left: 522px; top: 329px;
    width: 326px; height: 129px;
    background: var(--paper);
    display: flex;
    align-items: center;
    padding-left: 62px;
    gap: 12px;
  }
  .brand-dot {
    width: 34px; height: 34px;
    border-radius: 50%;
    background: var(--navy);
    flex: none;
  }
  .brand-name {
    font-weight: 500;
    font-size: 17px;
    line-height: 19px;
    color: var(--navy);
  }
  .content {
    position: absolute;
    left: 52px; top: 486px;
    width: 760px;
  }
  .lead {
    font-size: 32px;
    font-weight: 400;
    color: var(--green);
    line-height: 40px;
  }
  .positions {
    margin-top: 14px;
    font-size: 28.5px;
    font-weight: 700;
    color: var(--navy);
    line-height: 37px;
  }
  .section-title {
    font-size: 18px;
    font-weight: 700;
    letter-spacing: 0.2px;
    line-height: 24px;
    margin-top: 22px;
  }
  .list {
    list-style: none;
  }
  .list li {
    position: relative;
    padding-left: 51px;
    font-size: 18.5px;
    line-height: 25.7px;
  }
  .list li::before {
    content: "";
    position: absolute;
    left: 8px; top: 11px;
    width: 6px; height: 6px;
    border-radius: 50%;
    background: var(--ink);
  }
  .contact p {
    font-size: 18.5px;
    line-height: 25.7px;
  }
  .contact strong { font-weight: 500; }
</style>
</head>
<body>
  <main class="poster">
    <div class="hero-photo" role="img" aria-label="Foto: Zahnmedizinische Fachkraft mit Mundschutz und blauen Handschuhen hält Sonde und Mundspiegel"></div>

    <div class="brand-panel">
      <span class="brand-dot"></span>
      <span class="brand-name">Zahnarztpraxis<br>Tannbach</span>
    </div>

    <section class="content">
      <p class="lead">Wir suchen in Vollzeit:</p>
      <h1 class="positions">Zahnmedizinische Fachangestellte (m,w,d)<br>Zahnmedizinische Prophylaxeassistentin (m,w,d)</h1>

      <h2 class="section-title" style="margin-top:30px">DEINE VORTEILE</h2>
      <ul class="list">
        <li>Geregelte Arbeitszeiten</li>
        <li>Top moderne Ausstattung</li>
        <li>Spannende Mitarbeiterevents und Spaß bei der Arbeit</li>
        <li>Etabliertes Qualitätsmanagement und klare Strukturen</li>
        <li>Flexible Urlaubsplanung</li>
        <li>Überdurchschnittliches Gehalt</li>
        <li>Kostenfreie Zahnbehandlungen inkl. Bleaching</li>
      </ul>

      <h2 class="section-title">WAS UNS WICHTIG IST</h2>
      <ul class="list">
        <li>Du bist aufgeschlossen und motiviert</li>
        <li>Du bist kommunikativ und kontaktfreudig im Umgang mit Menschen</li>
        <li>Du hast Freude an deiner Arbeit</li>
        <li>Dann bist DU die Verstärkung die wir suchen!</li>
      </ul>

      <h2 class="section-title">INTERESSE ?</h2>
      <div class="contact">
        <p>Wir freuen uns über eine schriftliche Bewerbung</p>
        <p>per Post an: <strong>Dr. Harbeck, Lindenstr. 12, 73450 Tannbach</strong></p>
        <p>oder per Mail an: <strong>timo-harbeck@postfeld.de</strong></p>
      </div>
    </section>
  </main>
</body>
</html>
```